New start up pack

Looking for a business card design , letter head for tenders , invoices and contracts and an email signature. Logo attached.<br/>

Font styles to use
Sans Serif

Colors

Designer to choose colors to be used in the design.

Requirements
Nice to have
• Something different rather than just standard logo and text it

```html
<!DOCTYPE html>
<html lang="en">
<head>
<meta charset="utf-8">
<title>Ridgeline Holdings – Business Card</title>
<link href="https://fonts.googleapis.com/css2?family=Lato:ital,wght@0,400;0,700;0,900;1,400;1,900&display=swap" rel="stylesheet">
<style>
  :root {
    --stage: #2a2a2a;
    --brand-blue: #1a74c4;
    --pattern-blue: #2f86d2;
    --ink-grey: #555a60;
    --mark-grey: #7b7e82;
    --rule-blue: #9cc6ea;
    --paper: #ffffff;
  }
  * { box-sizing: border-box; margin: 0; padding: 0; }
  html, body {
    width: 1200px; height: 878px; overflow: hidden;
    background: var(--stage);
    font-family: "Lato", Arial, sans-serif;
  }
  .stage { position: relative; width: 1200px; height: 878px; }

  .card {
    position: absolute; width: 640px; height: 366px;
    box-shadow: 0 10px 30px rgba(0,0,0,.45);
    overflow: hidden;
  }

  /* Back side */
  .card-back { left: 280px; top: 48px; background: var(--brand-blue); }
  .back-pattern {
    position: absolute; inset: 0;
    background: linear-gradient(135deg, var(--pattern-blue), var(--brand-blue));
  }
  .back-name {
    position: absolute; right: 70px; top: 150px;
    color: var(--paper); font-weight: 900; font-size: 26px;
    letter-spacing: 1px; text-align: right; line-height: 1.05;
  }

  /* Front side */
  .card-front { left: 280px; top: 464px; background: var(--paper); }
  .holder { position: absolute; left: 34px; top: 34px; }
  .holder-name {
    color: var(--brand-blue); font-weight: 900; font-style: italic;
    font-size: 30px; line-height: 1;
  }
  .holder-title {
    color: var(--ink-grey); font-style: italic; font-size: 17px; margin-top: 4px;
  }

  .company {
    position: absolute; right: 44px; top: 168px; text-align: center;
    color: var(--brand-blue); font-weight: 900; line-height: 1.1;
  }
  .company-main { font-size: 36px; letter-spacing: .5px; }
  .company-sub { font-size: 15px; letter-spacing: 11px; margin-right: -11px; }

  .contacts { position: absolute; left: 40px; top: 236px; list-style: none; }
  .contacts li {
    display: flex; align-items: center; gap: 12px;
    color: var(--ink-grey); font-size: 17px; height: 23px;
  }
  .contacts svg { width: 14px; height: 14px; fill: var(--brand-blue); flex: none; }

  .rule {
    position: absolute; left: 34px; right: 50px; top: 312px;
    border-top: 1px solid var(--rule-blue);
  }
  .address {
    position: absolute; left: 34px; top: 318px;
    display: flex; align-items: center; gap: 12px;
    color: var(--ink-grey); font-size: 17px;
  }
  .address svg { width: 13px; height: 16px; fill: var(--brand-blue); }

  .base-band { position: absolute; left: 0; right: 0; bottom: 0; height: 12px; background: var(--brand-blue); }
  .base-band::before {
    content: ""; position: absolute; left: 0; top: 0; width: 34px; height: 12px; background: var(--mark-grey);
    border-right: 4px solid var(--paper);
  }
</style>
</head>
<body>
<main class="stage">

  <section class="card card-back" aria-label="Card back">
    <div class="back-pattern" role="img" aria-label="Repeating decorative pattern in blue tones"></div>
    <div class="back-name">RIDGELINE<br>HOLDINGS</div>
  </section>

  <section class="card card-front" aria-label="Card front">
    <div class="holder">
      <h1 class="holder-name">Maren Ellsworth</h1>
      <p class="holder-title">Founder &amp; CEO</p>
    </div>

    <div class="company">
      <div class="company-main">RIDGELINE</div>
      <div class="company-sub">HOLDINGS</div>
    </div>

    <ul class="contacts">
      <li>
        <svg viewBox="0 0 24 24" aria-hidden="true"><path d="M6.6 10.8a15.1 15.1 0 0 0 6.6 6.6l2.2-2.2a1 1 0 0 1 1-.25 11.4 11.4 0 0 0 3.6.57 1 1 0 0 1 1 1V20a1 1 0 0 1-1 1A17 17 0 0 1 3 4a1 1 0 0 1 1-1h3.5a1 1 0 0 1 1 1c0 1.25.2 2.45.57 3.57a1 1 0 0 1-.25 1z"/></svg>
        1234567890
      </li>
      <li>
        <svg viewBox="0 0 24 24" aria-hidden="true"><path d="M2 5h20v14H2z M2 5l10 8 10-8" fill="none" stroke="#1a74c4" stroke-width="2"/></svg>
        info@yourmail.com
      </li>
      <li>
        <svg viewBox="0 0 24 24" aria-hidden="true"><g fill="none" stroke="#1a74c4" stroke-width="1.8"><circle cx="12" cy="12" r="10"/><path d="M2 12h20M12 2c3 3 3 17 0 20M12 2c-3 3-3 17 0 20"/></g></svg>
        www.yourwebsite.com
      </li>
    </ul>

    <div class="rule"></div>

    <p class="address">
      <svg viewBox="0 0 20 26" aria-hidden="true"><path d="M10 0a9 9 0 0 0-9 9c0 7 9 17 9 17s9-10 9-17a9 9 0 0 0-9-9zm0 12.5A3.5 3.5 0 1 1 10 5.5a3.5 3.5 0 0 1 0 7z"/></svg>
      1234 First Line Address 5678 Second Line Address
    </p>

    <div class="base-band"></div>
  </section>

</main>
</body>
</html>
```